Verpackungsdesign für hochwertiges Haarparfum
Zielgruppe
Tovel's Method ist eine israelische Firma, die hochqualitative Haarprodukte und Haar Tools verkauft. Unsere Zielgruppe sind Frauen, die viel in Ihr Aussehen investieren und auf Ihr Äußeres sehr Wert legen.
Aufgabenstellung
Wir suchen nach einem Design für unsere zwei neuen Haarparfums. Es sollte teuer aussehen und das Design sollte modern und simpel sein. Die Flachen sind mit Milchglas und das Design wird auf die Flaschen gedruckt. Das Design muss komplett in Englischer Sprache sein.
Die Masse sind:
Höhe 7,7 cm
Umfang 11 cm
Es wird zwei Düfte geben.
1. The Nordic : Deckel wird Silber glänzend
2. The Celtic: Deckel wird Silber matt
Informationen die auf der Flasche sein sollten:
1. Firmen Logo (wird angehängt)
2. Name des Parfüms (The Nordic or the Celtic)
3. Longlasting Hair Fragrance
4. 30 ml
5. Includes essential hair vitamins and minerals
6. Alcohol and salt free

```html
<!DOCTYPE html>
<html lang="en">
<head>
<meta charset="utf-8">
<title>Tovel's Method – Lasting Hair Fragrance Labels</title>
<link rel="stylesheet" href="https://fonts.googleapis.com/css2?family=Playfair+Display:wght@500&family=IM+Fell+English:ital@0;1&family=Barlow+Condensed:wght@500&display=swap">
<style>
  :root {
    --paper: #ffffff;
    --frame: #b8b8b8;
    --ink: #141414;
    --logo-grey: #9a9a9a;
    --celtic: #4b3d38;
    --celtic-art: #d9d1ce;
    --nordic: #2a3670;
    --nordic-art: #c3cfec;
  }
  * { margin: 0; padding: 0; box-sizing: border-box; }
  html, body {
    width: 1200px; height: 1122px; overflow: hidden;
    background: var(--paper);
  }
  .label-sheet {
    display: flex;
    width: 1200px; height: 1122px;
  }
  .label {
    position: relative;
    width: 600px; height: 1122px;
    border: 2px solid var(--frame);
    background: var(--paper);
  }
  .label + .label { border-left-width: 1px; }
  .label > * { position: absolute; left: 50%; transform: translateX(-50%); text-align: center; }

  .brand-mark {
    top: 312px;
    display: flex; flex-direction: column; align-items: center; gap: 4px;
    font-family: 'Playfair Display', serif;
    font-weight: 500;
    font-size: 11px;
    letter-spacing: 1px;
    color: var(--logo-grey);
    white-space: nowrap;
  }
  .brand-mark .brand-square {
    width: 30px; height: 30px;
    border: 1.5px solid var(--logo-grey);
  }

  .scent-name {
    top: 372px;
    font-family: 'Playfair Display', serif;
    font-weight: 500;
    font-size: 60px;
    line-height: 1;
    white-space: nowrap;
  }
  .label--celtic .scent-name { color: var(--celtic); }
  .label--nordic .scent-name { color: var(--nordic); }

  .tagline {
    top: 444px;
    font-family: 'IM Fell English', serif;
    font-style: italic;
    font-size: 25px;
    color: var(--ink);
    white-space: nowrap;
  }
  .benefit {
    top: 478px;
    font-family: 'IM Fell English', serif;
    font-size: 16px;
    line-height: 1.05;
    color: var(--ink);
    white-space: nowrap;
  }

  .crystal-art {
    top: 540px;
    width: 100px; height: 145px;
  }
  .label--celtic .crystal-art { background: linear-gradient(160deg, var(--celtic-art), #efeae8); }
  .label--nordic .crystal-art { background: linear-gradient(160deg, var(--nordic-art), #eef2fb); }

  .free-badge {
    top: 730px; left: 38%;
    width: 34px; height: 34px;
  }
  .volume {
    top: 730px; left: 60%;
    font-family: 'Barlow Condensed', sans-serif;
    font-weight: 500;
    font-size: 24px;
    color: var(--ink);
    white-space: nowrap;
  }
</style>
</head>
<body>
  <main class="label-sheet">
    <section class="label label--celtic">
      <div class="brand-mark"><span class="brand-square"></span>Tovel's Method</div>
      <h1 class="scent-name">Celtic</h1>
      <p class="tagline">lasting hair fragrance</p>
      <p class="benefit">contains essential vitamins<br>and minerals for hair</p>
      <div class="crystal-art" role="img" aria-label="Line drawing of a cluster of crystals in warm grey-brown"></div>
      <svg class="free-badge" viewBox="0 0 34 34" aria-hidden="true">
        <circle cx="17" cy="17" r="15" fill="none" stroke="#141414" stroke-width="2"/>
      </svg>
      <p class="volume">30 ml</p>
    </section>

    <section class="label label--nordic">
      <div class="brand-mark"><span class="brand-square"></span>Tovel's Method</div>
      <h1 class="scent-name">Nordic</h1>
      <p class="tagline">lasting hair fragrance</p>
      <p class="benefit">contains essential vitamins<br>and minerals for hair</p>
      <div class="crystal-art" role="img" aria-label="Line drawing of tall crystal prisms in soft blue"></div>
      <svg class="free-badge" viewBox="0 0 34 34" aria-hidden="true">
        <circle cx="17" cy="17" r="15" fill="none" stroke="#141414" stroke-width="2"/>
      </svg>
      <p class="volume">30 ml</p>
    </section>
  </main>
</body>
</html>
```